BrightHarbor Flowchart Marketing Flyer

We are an MSP IT company. We have created a flowchart that we would like jazzed up to use in marketing new customers. The flowchart is a visual for prospective clients to see, in a simple way, what our process is. The flowchart should be 8.5"x11". We do not want the template of the flowchart altered (no boxes moved around) but would like something visually appealing and clean looking. Our office colors are lime green, royal blue, with accent colors of orange and purple. We would like the colors incorporated into the design. The design should be modern. This flyer is not going to be mass mailed. It will be handed to a prospective client in a face to face meeting.
Updates

I have uploaded our company logo to my brief in a couple of formats. One of the designers requested this. Great idea! I apologize for not providing it to begin with - it's my first time using this Website and the first time I have been assigned a project.

I was not able to view over the weekend as I did not have access to my work computer. Also need to review with the rest of management team on Thursday 6/28

Target Market(s)

Potential clients for an MSP IT company

Industry/Entity Type

It Company

Requirements
Must have
• The template itself we don't want changed. In other words we don't want the boxes moved around.
Nice to have
• Text, lines, shading and color of boxes can be changed. Not all colors mentioned in the brief need to be used. Would like it easy on the eye.

```html
<!DOCTYPE html>
<html lang="en">
<head>
<meta charset="utf-8">
<title>BrightHarbor Process Flyer</title>
<link href="https://fonts.googleapis.com/css2?family=Lato:wght@400;700;900&display=swap" rel="stylesheet">
<style>
  :root {
    --frame: #2a2a2c;
    --paper-light: #f4f6e2;
    --paper-edge: #d8dabd;
    --pink: #e8177a;
    --navy-top: #2e3d9e;
    --navy-bottom: #14124a;
    --navy-line: #1f2a8a;
    --green-top: #a2c93e;
    --green-bottom: #587a2a;
    --green-line: #8dbd3a;
    --orange-top: #f59c46;
    --orange-bottom: #a5632a;
    --magenta-top: #e61e82;
    --magenta-bottom: #6e1c5c;
    --connector: #555759;
    --panel: #f4f5f7;
    --ink: #333336;
    --white: #ffffff;
  }
  html, body { margin: 0; padding: 0; overflow: hidden; background: var(--frame); }
  .canvas { display: block; width: 1200px; height: 957px; }
  .title { font-family: 'Lato', sans-serif; font-weight: 900; font-size: 66px; fill: var(--pink); }
  .step-title { font-family: 'Lato', sans-serif; font-weight: 700; font-size: 25px; fill: var(--white); }
  .step-item { font-family: 'Lato', sans-serif; font-weight: 400; font-size: 19px; fill: var(--white); }
  .panel-heading { font-family: 'Lato', sans-serif; font-weight: 700; font-size: 29px; fill: var(--pink); }
  .cycle-label { font-family: 'Lato', sans-serif; font-weight: 700; font-size: 24px; fill: var(--white); }
  .panel-item { font-family: 'Lato', sans-serif; font-weight: 400; font-size: 19px; fill: var(--ink); }
  .connector { fill: none; stroke: var(--connector); stroke-width: 4; }
</style>
</head>
<body>
<svg class="canvas" viewBox="0 0 1500 1196" xmlns="http://www.w3.org/2000/svg" role="img" aria-label="BrightHarbor process flowchart">
  <defs>
    <radialGradient id="paper" cx="0.45" cy="0.5" r="0.75">
      <stop offset="0" stop-color="var(--paper-light)"/>
      <stop offset="1" stop-color="var(--paper-edge)"/>
    </radialGradient>
    <linearGradient id="navy" x1="0" y1="0" x2="0" y2="1">
      <stop offset="0" stop-color="var(--navy-top)"/><stop offset="1" stop-color="var(--navy-bottom)"/>
    </linearGradient>
    <linearGradient id="green" x1="0" y1="0" x2="0" y2="1">
      <stop offset="0" stop-color="var(--green-top)"/><stop offset="1" stop-color="var(--green-bottom)"/>
    </linearGradient>
    <linearGradient id="orange" x1="0" y1="0" x2="0" y2="1">
      <stop offset="0" stop-color="var(--orange-top)"/><stop offset="1" stop-color="var(--orange-bottom)"/>
    </linearGradient>
    <linearGradient id="navy-disc" x1="1" y1="0" x2="0" y2="1">
      <stop offset="0" stop-color="var(--navy-top)"/><stop offset="1" stop-color="var(--navy-bottom)"/>
    </linearGradient>
    <linearGradient id="green-disc" x1="1" y1="0" x2="0" y2="1">
      <stop offset="0" stop-color="var(--green-top)"/><stop offset="1" stop-color="var(--green-bottom)"/>
    </linearGradient>
    <linearGradient id="magenta-disc" x1="1" y1="0" x2="0" y2="1">
      <stop offset="0" stop-color="var(--magenta-top)"/><stop offset="1" stop-color="var(--magenta-bottom)"/>
    </linearGradient>
    <linearGradient id="orange-disc" x1="1" y1="0" x2="0" y2="1">
      <stop offset="0" stop-color="var(--orange-top)"/><stop offset="1" stop-color="var(--orange-bottom)"/>
    </linearGradient>
    <marker id="arrowhead" viewBox="0 0 10 10" refX="8" refY="5" markerWidth="5" markerHeight="5" orient="auto">
      <path d="M0 0 L10 5 L0 10 z" fill="var(--connector)"/>
    </marker>
  </defs>

  <rect class="frame" width="1500" height="1196" fill="var(--frame)"/>
  <rect class="flyer" x="107" y="100" width="1286" height="995" fill="url(#paper)"/>

  <g class="headline">
    <text class="title" x="188" y="270">BRIGHTHARBOR</text>
    <text class="title" x="188" y="348">PROCESS</text>
  </g>

  <g class="step step-assess">
    <rect x="170" y="405" width="348" height="178" rx="24" fill="var(--white)" stroke="var(--navy-line)" stroke-width="3"/>
    <rect x="176" y="411" width="336" height="166" rx="20" fill="url(#navy)"/>
    <text class="step-title" x="205" y="463">Assess Alignment</text>
    <text class="step-item" x="205" y="496">• Review Technology Philosophy</text>
    <text class="step-item" x="205" y="519">• Share Proprietary Method</text>
    <text class="step-item" x="205" y="543">• Assess Organizational Fit</text>
  </g>

  <g class="step step-onboarding">
    <rect x="170" y="610" width="348" height="178" rx="24" fill="var(--white)" stroke="var(--green-line)" stroke-width="3"/>
    <rect x="176" y="616" width="336" height="166" rx="20" fill="url(#green)"/>
    <text class="step-title" x="205" y="658">On Boarding</text>
    <text class="step-item" x="205" y="686">• Establish Expectations</text>
    <text class="step-item" x="205" y="709">• Service Provider Transition</text>
    <text class="step-item" x="205" y="733">• Cybersecurity Review</text>
    <text class="step-item" x="205" y="756">• Backup/Protection Strategy</text>
  </g>

  <g class="step step-evaluation">
    <rect x="170" y="815" width="348" height="178" rx="24" fill="var(--white)" stroke="var(--connector)" stroke-width="3"/>
    <rect x="176" y="821" width="336" height="166" rx="20" fill="url(#orange)"/>
    <text class="step-title" x="205" y="863">30 Day Evaluation</text>
    <text class="step-item" x="205" y="891">• Develop IT Playbook</text>
    <text class="step-item" x="205" y="914">• Major Risk Identification</text>
    <text class="step-item" x="205" y="938">• Observe &amp; Document Trends</text>
    <text class="step-item" x="205" y="961">• Standards Alignment Plan</text>
  </g>

  <g class="connectors">
    <path class="connector" d="M518 488 H608 V657 H704" marker-end="url(#arrowhead)"/>
    <path class="connector" d="M518 699 H704" marker-end="url(#arrowhead)"/>
    <path class="connector" d="M518 908 H608 V740 H704" marker-end="url(#arrowhead)"/>
    <circle cx="518" cy="488" r="8" fill="var(--navy-bottom)" stroke="var(--connector)" stroke-width="3"/>
    <circle cx="608" cy="488" r="8" fill="var(--navy-bottom)" stroke="var(--connector)" stroke-width="3"/>
    <circle cx="608" cy="657" r="8" fill="var(--navy-bottom)" stroke="var(--connector)" stroke-width="3"/>
    <circle cx="518" cy="699" r="8" fill="var(--green-top)" stroke="var(--connector)" stroke-width="3"/>
    <circle cx="518" cy="908" r="8" fill="var(--orange-top)" stroke="var(--connector)" stroke-width="3"/>
    <circle cx="608" cy="908" r="8" fill="var(--orange-top)" stroke="var(--connector)" stroke-width="3"/>
    <circle cx="608" cy="740" r="8" fill="var(--orange-top)" stroke="var(--connector)" stroke-width="3"/>
  </g>

  <g class="ongoing-panel">
    <rect x="740" y="202" width="593" height="792" rx="60" fill="var(--panel)" stroke="var(--connector)" stroke-width="4"/>
    <text class="panel-heading" x="1036" y="251" text-anchor="middle">Ongoing Strategic Plan &amp; Execution</text>

    <circle cx="1036" cy="565" r="175" fill="none" stroke="#6a6b6d" stroke-width="10"/>

    <g class="cycle-node">
      <circle cx="1036" cy="393" r="89" fill="var(--white)" stroke="var(--navy-line)" stroke-width="3"/>
      <circle cx="1036" cy="393" r="82" fill="url(#navy-disc)"/>
      <text class="cycle-label" x="1036" y="401" text-anchor="middle">Strategy</text>
    </g>
    <g class="cycle-node">
      <circle cx="866" cy="565" r="89" fill="var(--white)" stroke="var(--green-line)" stroke-width="3"/>
      <circle cx="866" cy="565" r="82" fill="url(#green-disc)"/>
      <text class="cycle-label" x="866" y="557" text-anchor="middle">Risk</text>
      <text class="cycle-label" x="866" y="583" text-anchor="middle">Assessment</text>
    </g>
    <g class="cycle-node">
      <circle cx="1206" cy="565" r="89" fill="var(--white)" stroke="var(--pink)" stroke-width="3"/>
      <circle cx="1206" cy="565" r="82" fill="url(#magenta-disc)"/>
      <text class="cycle-label" x="1210" y="557" text-anchor="middle">Standards</text>
      <text class="cycle-label" x="1210" y="583" text-anchor="middle">Alignment</text>
    </g>
    <g class="cycle-node">
      <circle cx="1036" cy="735" r="89" fill="var(--white)" stroke="var(--orange-top)" stroke-width="3"/>
      <circle cx="1036" cy="735" r="82" fill="url(#orange-disc)"/>
      <text class="cycle-label" x="1036" y="744" text-anchor="middle">Budget</text>
    </g>

    <text class="panel-item" x="853" y="864">• Develop &amp; Execute Annual Strategic Plan</text>
    <text class="panel-item" x="853" y="887">• Risk Assessment, Ranking, Mitigation</text>
    <text class="panel-item" x="853" y="910">• Prioritize Investments</text>
    <text class="panel-item" x="853" y="934">• Develop 5 Year Budget</text>
    <text class="panel-item" x="853" y="957">• HarborPathTM Standard Alignment</text>
  </g>
</svg>
</body>
</html>
```